Verindo Living- Hang tags for Modern Handmade Home Decor products

We need to design some hang tags to use for our products, we want double tags, meaning two tags that go together on one string, two different and coordinating sizes and shapes. We have a logo, what we need is the artwork for these two tags to take to print. One tag will have the logo on one side and company information on the other, the second tag will be for product information. For example, we specialize in handmade pieces from Latin America, on the product tag I want space to write the product info but also a line for what country it's from and what community created it. I'm attaching an image of the shapes of tags that I like, along with a copy of our logo. On the larger company tag I'd like our logo in the center and a color block stripe of the yellow color of our logo at the bottom, on the flip side there will just be text, sort of our company motto. On the narrower longer product info tag I'd like a small logo at the bottom end and space for product information to be written in by hand and on the flip side of this one lines for what country it's from, what community created it and care instructions, again, all information that we will write in by hand. Please let me know if you have questions.

Target Market(s)

Design savvy, house proud, well educated people who travel and appreciate art.

Font styles to use
Sans Serif

Requirements
Must have
• I want it to look graphic, sophisticated and modern. I want to be very legible and clean.
Nice to have
• Clarity, easy to read, and maybe a bit of whimsy or lightheartedness.
Should not have
• Nothing that feels "ethnic" or "crafty:, even though our products are handmade in Latin America they are contemporary and sophisticated, not stereotypical.

```html
<!DOCTYPE html>
<html lang="en">
<head>
<meta charset="utf-8">
<title>Verindo Living — Hang Tags</title>
<link href="https://fonts.googleapis.com/css2?family=Questrial&display=swap" rel="stylesheet">
<style>
  :root {
    --backdrop: #929394;
    --tag-white: #ffffff;
    --brand-yellow: #f5c11b;
    --ink-grey: #98a2a7;
    --band-text: #ffffff;
  }
  * { margin: 0; padding: 0; box-sizing: border-box; }
  html, body { width: 1200px; height: 1000px; overflow: hidden; }
  body {
    background: var(--backdrop);
    font-family: "Questrial", "Helvetica Neue", Arial, sans-serif;
    color: var(--ink-grey);
    position: relative;
  }
  .tag {
    position: absolute;
    background: var(--tag-white);
  }
  .tag--company {
    width: 185px; height: 259px; top: 259px;
    clip-path: polygon(16px 0, 169px 0, 185px 20px, 185px 100%, 0 100%, 0 20px);
  }
  .tag--product {
    width: 167px; height: 471px; top: 47px;
    clip-path: polygon(33px 0, 134px 0, 167px 48px, 167px 100%, 0 100%, 0 48px);
  }
  .tag--company-front { left: 153px; }
  .tag--company-back  { left: 375px; }
  .tag--product-front { left: 606px; }
  .tag--product-back  { left: 809px; }

  .color-band {
    position: absolute; left: 0; right: 0; bottom: 0; height: 32px;
    background: var(--brand-yellow);
    color: var(--band-text);
    font-size: 11px; letter-spacing: 0.08em;
    display: flex; align-items: center; justify-content: center;
  }
  .motto {
    position: absolute; left: 17px; right: 8px;
    font-size: 11.5px; line-height: 14.5px; letter-spacing: 0.05em;
  }
  .tag--product .motto { left: 9px; right: 8px; }
  .motto p + p { margin-top: 14.5px; }
  .motto__line {
    display: block; white-space: nowrap;
    text-align: justify; text-align-last: justify;
  }
  .motto__line--last { text-align-last: left; }

  .brand-mark {
    position: absolute; left: 0; right: 0;
    display: flex; flex-direction: column; align-items: center;
  }
  .brand-mark__dot { background: var(--brand-yellow); border-radius: 50%; }
  .brand-mark__name { color: var(--ink-grey); letter-spacing: 0.03em; white-space: nowrap; line-height: 1.1; }
  .brand-mark__url { letter-spacing: 0.15em; white-space: nowrap; line-height: 1; }

  .brand-mark--large { top: 68px; }
  .brand-mark--large .brand-mark__dot { width: 52px; height: 52px; margin-bottom: 14px; }
  .brand-mark--large .brand-mark__name { font-size: 22px; }
  .brand-mark--large .brand-mark__url { font-size: 6px; margin-top: 5px; }

  .brand-mark--small .brand-mark__dot { width: 12px; height: 12px; margin-bottom: 4px; }
  .brand-mark--small .brand-mark__name { font-size: 8px; }

  .brand-mark--medium .brand-mark__dot { width: 24px; height: 24px; margin-bottom: 6px; }
  .brand-mark--medium .brand-mark__name { font-size: 12px; }
  .brand-mark--medium .brand-mark__url { font-size: 5px; margin-top: 3px; }
</style>
</head>
<body>

  <section class="tag tag--company tag--company-front">
    <div class="brand-mark brand-mark--large">
      <span class="brand-mark__dot"></span>
      <span class="brand-mark__name">Verindo Living</span>
      <span class="brand-mark__url">www.verindoliving.com</span>
    </div>
    <div class="color-band">MADE IN USA</div>
  </section>

  <section class="tag tag--company tag--company-back">
    <div class="motto" style="top:46px;">
      <p>
        <span class="motto__line">Lorem ipsum dolor sit</span>
        <span class="motto__line">amet, consectetur</span>
        <span class="motto__line">adipiscing elit. Proin</span>
        <span class="motto__line">accumsan diam sed</span>
        <span class="motto__line">arcu ultricies, semper</span>
        <span class="motto__line">interdum odio laoreet.</span>
        <span class="motto__line">In eget ullamcorper</span>
        <span class="motto__line motto__line--last">nisi. felis.</span>
      </p>
    </div>
    <div class="brand-mark brand-mark--small" style="top:194px;">
      <span class="brand-mark__dot"></span>
      <span class="brand-mark__name">Verindo Living</span>
    </div>
    <div class="color-band">your text here</div>
  </section>

  <section class="tag tag--product tag--product-front">
    <div class="motto" style="top:78px;">
      <p>
        <span class="motto__line">Lorem ipsum dolor sit</span>
        <span class="motto__line">amet, consectetur</span>
        <span class="motto__line">adipiscing elit. Proin</span>
        <span class="motto__line">accumsan diam sed</span>
        <span class="motto__line">arcu ultricies, semper</span>
        <span class="motto__line">interdum odio laoreet.</span>
        <span class="motto__line">In eget ullamcorper</span>
        <span class="motto__line motto__line--last">nisi. felis.</span>
      </p>
      <p>
        <span class="motto__line">Lorem ipsum dolor sit</span>
        <span class="motto__line">amet, consectetur</span>
        <span class="motto__line">adipiscing elit. Proin</span>
        <span class="motto__line">accumsan diam sed</span>
        <span class="motto__line">arcu ultricies, semper</span>
        <span class="motto__line">interdum odio laoreet.</span>
        <span class="motto__line">In eget ullamcorper</span>
        <span class="motto__line motto__line--last">nisi. felis.</span>
      </p>
    </div>
    <div class="brand-mark brand-mark--medium" style="top:382px;">
      <span class="brand-mark__dot"></span>
      <span class="brand-mark__name">Verindo Living</span>
      <span class="brand-mark__url">www.verindoliving.com</span>
    </div>
    <div class="color-band">MADE IN USA</div>
  </section>

  <section class="tag tag--product tag--product-back">
    <div class="brand-mark brand-mark--medium" style="top:54px;">
      <span class="brand-mark__dot"></span>
      <span class="brand-mark__name">Verindo Living</span>
      <span class="brand-mark__url">www.verindoliving.com</span>
    </div>
    <div class="motto" style="top:139px;">
      <p>
        <span class="motto__line">Lorem ipsum dolor sit</span>
        <span class="motto__line">amet, consectetur</span>
        <span class="motto__line">adipiscing elit. Proin</span>
        <span class="motto__line">accumsan diam sed</span>
        <span class="motto__line">arcu ultricies, semper</span>
        <span class="motto__line">interdum odio laoreet.</span>
        <span class="motto__line">In eget ullamcorper</span>
        <span class="motto__line motto__line--last">nisi. felis.</span>
      </p>
      <p>
        <span class="motto__line">Lorem ipsum dolor sit</span>
        <span class="motto__line">amet, consectetur</span>
        <span class="motto__line">adipiscing elit. Proin</span>
        <span class="motto__line">accumsan diam sed</span>
        <span class="motto__line">arcu ultricies, semper</span>
        <span class="motto__line">interdum odio laoreet.</span>
        <span class="motto__line">In eget ullamcorper</span>
        <span class="motto__line motto__line--last">nisi. felis.</span>
      </p>
    </div>
    <div class="color-band">your text here</div>
  </section>

</body>
</html>
```